dulvox presentation

I would like to improve the presentation of the PoweePoint. That attached.

Target Market(s)

Hotel sector - laboratories - industry

Font styles to use
Other font styles liked:
• como las del diseño

Requirements
Must have
• This PowerPoint. it has to serve as a company presentation.
Nice to have
• I wish it were pleasant to read. with background images or photographs that reinforce the text.

```html
<!DOCTYPE html>
<html lang="ca">
<head>
<meta charset="utf-8">
<title>Dulvox – Presentació dels serveis</title>
<link href="https://fonts.googleapis.com/css2?family=Roboto:ital,wght@0,300;0,400;0,500;0,700;0,900;1,400&family=Open+Sans:wght@400;600&display=swap" rel="stylesheet">
<style>
:root{
  --navy:#2d3850;
  --blue:#2c4a8c;
  --brand:#1b6dc1;
  --red:#f04848;
  --red-deep:#e3262b;
  --grey:#9b9b9b;
  --text:#555;
  --rule:#d6d6d6;
}
*{margin:0;padding:0;box-sizing:border-box}
html,body{width:1200px;height:3632px;overflow:hidden;background:#fff;font-family:Roboto,sans-serif;color:var(--text)}
.canvas{position:relative;width:1200px;height:3632px}
.abs{position:absolute}
.rule{position:absolute;left:0;width:1200px;height:2px;background:var(--rule)}
.mark{font-family:Roboto,sans-serif;font-weight:700;color:var(--brand);letter-spacing:2px;text-transform:uppercase}
.mark-small{position:absolute;left:0;width:1200px;text-align:center;font-size:22px}
/* cover */
.cover-photo{left:0;top:0;width:766px;height:687px;background:linear-gradient(120deg,#b9bcc0,#8f9398 55%,#c9c2b8)}
.cover-side{left:777px;top:0;width:423px;height:687px;background:linear-gradient(180deg,#d3d4d6,#b4b7bb)}
.cover-bar{left:766px;top:0;width:11px;height:687px;background:var(--red-deep)}
.cover-mark{left:803px;top:48px;font-size:72px;line-height:1;letter-spacing:6px}
.tagline{left:803px;top:145px;font-size:14px;font-weight:700;color:#6b6f75}
.cover-title{left:803px;top:222px;font-family:'Open Sans',sans-serif;font-size:33px;color:var(--red-deep)}
.cover-url{left:803px;top:636px;font-size:18px;font-weight:700;color:var(--red-deep)}
/* intro */
.slide-title{position:absolute;left:0;width:1200px;text-align:center;font-size:45px;font-weight:500;color:#555}
.item{position:absolute;left:130px;display:flex;align-items:center;height:80px}
.item .num{width:113px;font-size:64px;font-weight:900}
.item .label{font-size:23px;font-weight:500;color:#555}
/* areas */
.lead{position:absolute;left:103px;top:1648px;white-space:nowrap;font-size:19px;color:#555}
.lead b{color:#333}
.lead strong{color:var(--red-deep)}
.tile{position:absolute;top:1729px;height:311px;display:flex;align-items:center;padding-left:9px;color:#fff;font-size:24px;font-weight:700;white-space:nowrap;overflow:hidden}
/* services */
.svc-intro{position:absolute;left:13px;top:2298px;font-size:18px;color:#555;white-space:nowrap}
.svc-photo{position:absolute;left:0;width:451px}
.dot{position:absolute;left:407px;width:72px;height:72px;border-radius:50%}
.svc{position:absolute;left:492px;width:700px}
.svc h3{font-size:27px;font-weight:500;margin-bottom:8px}
.svc p{font-size:16px;font-weight:300;line-height:1.3;color:#555}
/* thanks */
.thanks-bg{left:0;top:2936px;width:1195px;height:696px;background:linear-gradient(115deg,#c8cbcf,#a2a7ad 50%,#d5d6d8)}
.thanks-frame{left:49px;top:2985px;width:451px;height:582px;border:11px solid var(--red-deep);background:rgba(255,255,255,.9)}
.thanks-inner{position:absolute;left:119px;top:3075px;width:320px}
.thanks-big{font-size:44px;font-weight:900;color:var(--brand);letter-spacing:1px}
.thanks-big span{display:inline-block;width:46px;border-bottom:1px solid #555;margin-left:10px}
.thanks-ca{margin-top:68px;font-size:28px;font-weight:500;color:#555}
.person{margin-top:26px;font-size:25px;font-weight:500;color:#555}
.role{font-size:18px;font-weight:700;color:#444}
.contact{margin-top:28px;padding-top:16px;border-top:1px solid #e4e4e4;font-size:18px;font-weight:300;color:#555;line-height:1.3}
.url{margin-top:22px;font-size:18px;font-weight:700;color:#444}
.thanks-mark{left:515px;top:3218px;font-size:130px;line-height:1;letter-spacing:10px}
</style>
</head>
<body>
<div class="canvas">

  <!-- cover -->
  <div class="abs cover-photo" role="img" aria-label="Photo of two engineers in hard hats reviewing plans at an industrial site"></div>
  <div class="abs cover-side" role="img" aria-label="Faded photo of industrial silos"></div>
  <div class="abs cover-bar"></div>
  <div class="abs mark cover-mark">DULVOX</div>
  <div class="abs tagline">REALITZEM I CUIDEM LES TEVES INSTAL·LACIONS</div>
  <div class="abs cover-title">Presentación del serveis</div>
  <div class="abs cover-url">www.dulvox.com</div>
  <div class="rule" style="top:686px"></div>

  <!-- introduction -->
  <div class="slide-title" style="top:770px;left:47px">INTRODUCCIÓN</div>
  <div class="item" style="top:894px"><span class="num" style="color:var(--navy)">01</span><span class="label">Les nostres principals àrees d'acció</span></div>
  <div class="item" style="top:1003px"><span class="num" style="color:var(--blue)">02</span><span class="label">Instal·lacions amb valor afegit</span></div>
  <div class="item" style="top:1116px"><span class="num" style="color:var(--red)">03</span><span class="label">Anticipar-se. Solucionar. Mantenir</span></div>
  <div class="item" style="top:1219px"><span class="num" style="color:var(--grey)">04</span><span class="label">La satisfacció dels nostres clients és el nostre major aval</span></div>
  <div class="mark mark-small" style="top:1355px;left:38px">DULVOX</div>
  <div class="rule" style="top:1412px"></div>

  <!-- areas -->
  <div class="mark mark-small" style="top:1439px;left:40px">DULVOX</div>
  <div class="slide-title" style="top:1517px;left:62px">ÀREES D'ACCIO</div>
  <div class="lead">A <b>DULVOX</b> tenim un <i>leitmotiv</i> que ens acompanya dia rere dia, any rere any: <strong>oferir un servei prèmium per a clients selectes</strong></div>
  <div class="tile" role="img" aria-label="Hotel lobby photo tinted blue" style="left:56px;width:311px;background:linear-gradient(180deg,#5d86aa,#4b77a0)">HOTELS I RESTAURANTS</div>
  <div class="tile" role="img" aria-label="Residential building photo tinted blue" style="left:367px;width:300px;background:linear-gradient(180deg,#5a82d2,#4a70c0);padding-left:90px">RESIDÈNCIES</div>
  <div class="tile" role="img" aria-label="Office interior photo tinted red" style="left:667px;width:316px;background:linear-gradient(180deg,#f57a7a,#ee6464);padding-left:103px">OFICINES</div>
  <div class="tile" role="img" aria-label="Shop photo tinted grey" style="left:983px;width:217px;background:linear-gradient(180deg,#8f8f8f,#7d7878);padding-left:82px">COMERÇOS</div>
  <div class="rule" style="top:2110px"></div>

  <!-- services -->
  <div class="mark mark-small" style="top:2173px;left:10px">DULVOX</div>
  <div class="slide-title" style="top:2221px;left:11px">SERVIES</div>
  <div class="svc-intro">A DULVOX estem en constant compromís amb la superació. Aquests són només alguns exemples dels serveis que oferim als nostres clients:</div>
  <div class="svc-photo" role="img" aria-label="Photo of a technician servicing an outdoor air conditioning unit" style="top:2345px;height:244px;background:linear-gradient(120deg,#bfc3c7,#8e969e 55%,#b8a98a)"></div>
  <div class="svc-photo" role="img" aria-label="Photo of a technician with a laptop at an electrical panel" style="top:2589px;height:245px;background:linear-gradient(120deg,#d7d9db,#5c6a80 50%,#4a4e55)"></div>
  <div class="dot" style="top:2363px;background:var(--navy)"></div>
  <div class="dot" style="top:2473px;background:var(--blue)"></div>
  <div class="dot" style="top:2624px;background:var(--red)"></div>
  <div class="dot" style="top:2731px;background:#bdbdbd"></div>
  <div class="svc" style="top:2366px"><h3 style="color:var(--navy)">LABORATORIS NORVEL</h3><p>Legalització i adaptació de les plantes refredadores. Instal·lació d'unitats UTA a la zona packaging.</p></div>
  <div class="svc" style="top:2477px"><h3 style="color:var(--blue)">HOTEL CALIU I HOTEL BRISA</h3><p>Canvi de sala de calderes de producció semiinstantània. Estalvi previst: 30 % en electricitat i 35 % en gas, segons el projecte d'eficiència energètica.</p></div>
  <div class="svc" style="top:2628px"><h3 style="color:var(--red)">VELMARA</h3><p>Manteniment correctiu i preventiu.</p></div>
  <div class="svc" style="top:2735px"><h3 style="color:var(--grey)">HOTEL SERRAT</h3><p>Canvi de l'antic sistema de calderes amb acumulació per un sistema de producció d'ACS semiinstantani. Fins al moment portem el 38 % d'estalvi en la factura de gas.</p></div>
  <div class="rule" style="top:2934px"></div>

  <!-- thanks -->
  <div class="abs thanks-bg" role="img" aria-label="Faded photo of a team joining fists together"></div>
  <div class="abs mark thanks-mark">DULVOX</div>
  <div class="abs thanks-frame"></div>
  <div class="thanks-inner">
    <div class="thanks-big">THANK YOU<span></span></div>
    <div class="thanks-ca">MOLTES GRÀCIES</div>
    <div class="person">Marc Vidal Serra</div>
    <div class="role">Enginyer Industrial &nbsp;I&nbsp; CEO</div>
    <div class="contact">+34 600 000 000<br>C. de l'Exemple, 14,<br>08000 - Ciutat</div>
    <div class="url">www.dulvox.com</div>
  </div>

</div>
</body>
</html>
```